Keep Climbing - Nobody Writes My Ending

The front book cover. The book will include life lessons I've learned through three breast cancer (Teal Lantern) diagnoses and how to create positivity through adversity. Lessons that most people don't think of until they're hit with a life-altering setback. The chapters include Imposter Syndrome (Teal Lantern Warriors don't have time to debate if they're good enough, they just jump in and get it done because life is too short), Stand Your Ground (stick up for your beliefs and advocate for yourself), The Flip Side of It's All About Me (like an emergency rescuer who must equip themselves first, you need to take care of yourself first). The main message in the book is when others say you CAN'T, I say you CAN! Warrior means being strong no matter what life deals you. I've included a word document with more information.

Please note: Pink is only to be an accent color. I'd like my brand colors to be included. The title of the book is to be the focus with an image to add to the book cover appeal.

Target Market(s)

professionals with a growth mindset and people going through adversity

Industry/Entity Type

HR, Libraries, Hosppitality,

Font styles to use
Sans Serif

Colors
6B429C
8869AF
B7A5CE
E3DAEB
F3F0F8

Requirements
Must have
• Be original. Cover to be appealing to male and female buyers. Incorporate my purple brand color. Be creative and unique.
Nice to have
• Although I have offered a suggestion, I'm open to a creative cover that wows me.
Should not have
• No cartoon image or stock image

```html
<!DOCTYPE html>
<html lang="en">
<head>
<meta charset="utf-8">
<title>Keep Climbing - Nobody Writes My Ending</title>
<link rel="stylesheet" href="https://fonts.googleapis.com/css2?family=Josefin+Sans:wght@600;700&family=Poiret+One&display=swap">
<style>
  :root {
    --brand-purple: #6B429C;
    --brand-violet: #8869AF;
    --brand-lilac: #B7A5CE;
    --brand-mist: #E3DAEB;
    --brand-white: #F3F0F8;
    --accent-pink: #B8489A;
    --text-white: #FFFFFF;
  }
  html, body {
    margin: 0;
    padding: 0;
    width: 750px;
    height: 1200px;
    overflow: hidden;
    background: var(--brand-lilac);
  }
  .cover {
    position: relative;
    width: 750px;
    height: 1200px;
    overflow: hidden;
    background: var(--brand-lilac);
  }
  .cover-art {
    position: absolute;
    inset: 0;
    background: radial-gradient(ellipse at 50% 40%, #BEADD3 0%, #B7A5CE 55%, #B3A0CB 100%);
  }
  .cover-graphic {
    position: absolute;
    inset: 0;
  }
  .title-main {
    font-family: "Josefin Sans", sans-serif;
    font-weight: 700;
    fill: var(--text-white);
    filter: drop-shadow(0 0 5px rgba(40, 15, 70, 0.6));
  }
  .subtitle-light {
    font-family: "Poiret One", sans-serif;
    font-size: 28px;
    fill: var(--text-white);
  }
  .subtitle-accent {
    font-family: "Poiret One", sans-serif;
    font-size: 38px;
    font-weight: 400;
    fill: var(--accent-pink);
    stroke: var(--text-white);
    stroke-width: 4px;
    stroke-linejoin: round;
    paint-order: stroke fill;
  }
  .author {
    position: absolute;
    left: 70px;
    top: 1050px;
    margin: 0;
    font-family: "Poiret One", sans-serif;
    font-weight: 400;
    color: var(--text-white);
    line-height: 1;
  }
  .author-name {
    display: block;
    font-size: 66px;
    letter-spacing: 1px;
  }
  .author-credentials {
    display: block;
    margin: -6px 0 0 248px;
    font-size: 29px;
    letter-spacing: 0.5px;
    color: var(--text-white);
  }
</style>
</head>
<body>
  <main class="cover">
    <div class="cover-art" role="img" aria-label="Soft glowing line drawing of a woman's torso outline"></div>

    <svg class="cover-graphic" width="750" height="1200" viewBox="0 0 750 1200" xmlns="http://www.w3.org/2000/svg">
      <g class="title-circles" fill="var(--brand-purple)" fill-opacity="0.93">
        <circle cx="195" cy="531" r="243"/>
        <circle cx="612" cy="443" r="243"/>
      </g>

      <g class="title-block" transform="translate(385 520) rotate(-15)">
        <text class="title-main" x="0" y="-40" font-size="68" text-anchor="middle">KEEP CLIMBING</text>
        <text class="title-main" x="0" y="12" font-size="40" text-anchor="middle">NOBODY WRITES MY ENDING</text>
        <text x="0" y="64" text-anchor="middle">
          <tspan class="subtitle-light">LIFE LESSONS FROM A </tspan><tspan class="subtitle-accent">3X TEAL WARRIOR</tspan>
        </text>
      </g>
    </svg>

    <h2 class="author">
      <span class="author-name">DL MARCHETTI</span>
      <span class="author-credentials">CCMS, MCVP, CSP</span>
    </h2>
  </main>
</body>
</html>
```